Redesign two student school awards

I need to redesign 2 students awards. I need the elements of the letterhead to be incorporated into the Student Awards. I have covered some of the letterhead elements to show just the 4 elements that need to be incorporated: school emblem, school name, "Strive with heart, serve with hope.", and the 3 coloured ribbon. The awards need to be in colour and the use of the 3 school colours - purple, yellow (gold) and chocolate brown,

I have upload the 2 awards the school presents to students (they are printed on A4 Paper). The first one is the:

(1) Year Adviser Award - this award needs to include the school name; the title: Year Adviser's Award; Award to; Name (where the word is deleted and the office staff type the students name or uploaded names which can be autofilled); for the following achievements; the year (which can be changed an include the day and month (but auto filled); Year Adviser (where the teacher signs their name - see lower left of the award; (also the 5 categories - School Service, Community Service , Sporting Achievements, Leadership, Academic Achievement (these 5 categories must be able to be deleted as a student may receive the Year Adviser's Award for 1 or 2 of the categories)

(2) Principal's Award - all elements of this award need to be included. In this example there's a fake name Luke Dawson - this is where the office staff type in the students name or hopefully upload a list of names that are auto filled. The 5 categories need to be retained e.g. School Service, Community Service etc (these can be fixed as they are not deleted; for the following achievements; the year (which can be changed an include the day and month (but auto filled); my name and title,

For the 2 student awards it would be good if the design is in a computer program where the office staff can auto fill students names.

The main goal is to redesign the 2 awards, whilst retaining current elements and include 4 of the elements from the letter head.

Target Market(s)

School students (12 years old to 18 years old)

Industry/Entity Type

Education

Font styles to use
Serif

Requirements
Must have
• The elements and school colours mentioned in the description. Would be helpful if the computer program it is contained in allows for auto fill of student names, date, and for the Year Advisers award any one of the five award categories can be removed. To be printed on A4 paper/card

Colours must contain the school colours as mentioned before and the 4 elements of the letterhead. I am trying to have all our communications and awards contain similar elements.

```html
<!DOCTYPE html>
<html lang="en">
<head>
<meta charset="utf-8">
<title>Student Awards – Principal's Award and Year Adviser's Award</title>
<link rel="stylesheet" href="https://fonts.googleapis.com/css2?family=Montserrat:wght@500;600&family=EB+Garamond:ital@1&display=swap">
<style>
  :root {
    --board: #2b2b2b;
    --paper: #ffffff;
    --purple: #9b3c8c;
    --yellow: #fff200;
    --chocolate: #3a1420;
    --ribbon: #5a1e2e;
    --ribbon-end: #e6dc9c;
    --ink: #3b1220;
    --note: #ffffff;
  }
  * { box-sizing: border-box; margin: 0; padding: 0; }
  html, body { width: 1200px; height: 848px; overflow: hidden; }
  body {
    background: var(--board);
    font-family: "Montserrat", "Century Gothic", sans-serif;
    color: var(--ink);
    position: relative;
  }
  .award {
    position: absolute;
    top: 28px;
    width: 474px;
    height: 673px;
    background: var(--paper);
    overflow: hidden;
  }
  .award--principal { left: 90px; }
  .award--adviser { left: 634px; }
  .award__trim { position: absolute; inset: 0; width: 100%; height: 100%; }
  .award__school {
    position: absolute; top: 33px; left: 0; width: 100%;
    padding-left: 20px;
    text-align: center; font-size: 14px; font-weight: 600; letter-spacing: 0.2px;
  }
  .award__emblem {
    position: absolute; top: 62px; left: 50%; transform: translateX(-40%);
    display: flex; flex-direction: column; align-items: center; gap: 6px;
  }
  .award__emblem-dot {
    width: 84px; height: 84px; border-radius: 50%; background: var(--purple);
  }
  .award__emblem-name { font-size: 15px; font-weight: 600; color: var(--purple); letter-spacing: 2px; }
  .award__ribbon { position: absolute; top: 186px; left: 42px; width: 392px; height: 63px; }
  .award__ribbon svg { width: 100%; height: 100%; display: block; }
  .award__title {
    position: absolute; left: 0; right: 0; top: 20px;
    text-align: center; color: var(--paper); font-weight: 500; font-size: 19px; letter-spacing: 0.5px;
  }
  .award--adviser .award__title { font-size: 17px; }
  .award__label {
    position: absolute; left: 0; width: 100%; padding-left: 20px;
    text-align: center; font-size: 14px; font-weight: 500;
  }
  .award__label--to { top: 280px; }
  .award__label--for { top: 372px; font-size: 13px; }
  .award__categories {
    position: absolute; left: 0; width: 100%; padding-left: 20px;
    list-style: none; text-align: center; font-weight: 500;
  }
  .award--principal .award__categories { top: 413px; font-size: 19px; line-height: 27.5px; letter-spacing: 0.5px; }
  .award--adviser .award__categories { top: 406px; font-size: 16px; line-height: 24.3px; letter-spacing: 0.3px; }
  .award__motto {
    position: absolute; top: 574px; left: 0; width: 100%; padding-left: 20px;
    text-align: center; font-family: "EB Garamond", Georgia, serif; font-style: italic; font-size: 21px;
  }
  .award__signatory, .award__date {
    position: absolute; top: 636px; font-size: 12px; font-weight: 500;
  }
  .award--principal .award__signatory { left: 36px; }
  .award--adviser .award__signatory { left: 133px; }
  .award__date { right: 82px; }
  .board-note {
    position: absolute; top: 731px; left: 0; width: 100%;
    text-align: center; color: var(--note); font-size: 21px; font-weight: 600;
    line-height: 39px; letter-spacing: 0.5px; text-transform: uppercase;
  }
</style>
</head>
<body>

<section class="award award--principal">
  <svg class="award__trim" viewBox="0 0 474 673" preserveAspectRatio="none" aria-hidden="true">
    <path d="M0 0 H51 L8 520 L0 570 Z" fill="var(--purple)"/>
    <path d="M0 673 V560 L30 360 L15 673 Z" fill="var(--yellow)"/>
    <path d="M474 160 V673 H418 Z" fill="var(--yellow)"/>
    <path d="M474 300 V673 H430 Z" fill="var(--chocolate)"/>
  </svg>
  <p class="award__school">GLENVALE MEMORIAL HIGH SCHOOL</p>
  <div class="award__emblem">
    <span class="award__emblem-dot"></span>
    <span class="award__emblem-name">GLENVALE</span>
  </div>
  <div class="award__ribbon">
    <svg viewBox="0 0 392 63" aria-hidden="true">
      <path d="M0 24 H64 V58 H0 L16 41 Z" fill="var(--ribbon-end)"/>
      <path d="M392 24 H328 V58 H392 L376 41 Z" fill="var(--ribbon-end)"/>
      <path d="M40 14 Q196 -8 352 14 V50 Q196 28 40 50 Z" fill="var(--ribbon)"/>
    </svg>
    <p class="award__title">PRINCIPAL'S AWARD</p>
  </div>
  <p class="award__label award__label--to">AWARDED TO</p>
  <p class="award__label award__label--for">FOR THE FOLLOWING ACHIEVEMENTS:</p>
  <ul class="award__categories">
    <li>SCHOOL SERVICE</li>
    <li>COMMUNITY SERVICE</li>
    <li>SPORTING ACHIEVEMENT</li>
    <li>LEADERSHIP</li>
    <li>ACADEMIC ACHIEVEMENT</li>
  </ul>
  <p class="award__motto">"Strive with heart, serve with hope."</p>
  <p class="award__signatory">PRINCIPAL:&nbsp; MR R. HOLLOWAY</p>
  <p class="award__date">05-21-20</p>
</section>

<section class="award award--adviser">
  <svg class="award__trim" viewBox="0 0 474 673" preserveAspectRatio="none" aria-hidden="true">
    <path d="M0 0 H55 C30 150 10 300 0 440 Z" fill="var(--purple)"/>
    <path d="M62 0 H80 C42 160 18 300 26 480 C14 330 28 160 62 0 Z" fill="var(--yellow)"/>
    <path d="M0 420 C25 500 40 600 55 673 H0 Z" fill="var(--chocolate)"/>
  </svg>
  <p class="award__school">GLENVALE MEMORIAL HIGH SCHOOL</p>
  <div class="award__emblem">
    <span class="award__emblem-dot"></span>
    <span class="award__emblem-name">GLENVALE</span>
  </div>
  <div class="award__ribbon">
    <svg viewBox="0 0 392 63" aria-hidden="true">
      <path d="M0 24 H64 V58 H0 L16 41 Z" fill="var(--ribbon-end)"/>
      <path d="M392 24 H328 V58 H392 L376 41 Z" fill="var(--ribbon-end)"/>
      <path d="M40 14 Q196 -8 352 14 V50 Q196 28 40 50 Z" fill="var(--ribbon)"/>
    </svg>
    <p class="award__title">YEAR ADVISER'S AWARD</p>
  </div>
  <p class="award__label award__label--to">AWARDED TO</p>
  <p class="award__label award__label--for">FOR THE FOLLOWING ACHIEVEMENTS:</p>
  <ul class="award__categories">
    <li>«SCHOOL SERVICE»</li>
    <li>«COMMUNITY SERVICE»</li>
    <li>«SPORTING ACHIEVEMENT»</li>
    <li>«LEADERSHIP»</li>
    <li>«ACADEMIC ACHIEVEMENT»</li>
  </ul>
  <p class="award__motto">"Strive with heart, serve with hope."</p>
  <p class="award__signatory">YEAR ADVISER</p>
  <p class="award__date">05-21-20</p>
</section>

<p class="board-note">Note: will provide a ready to edit publisher file (fill-in)<br>so you can easily edit the names, awards, date, and teacher:)</p>

</body>
</html>
```